Tidal Hounds Dog Behaviour, Training and Natural Healthcare Business Card Design

I am an experienced and qualified dog behavioural trainer and natural animal healthcare consultant offering a range of services to help pet dog owners with the "whole dog".
COLOURS: A soft light blue in the background - can be fading out or split, red should also feature
LOGO: Dog, healing hands, silhouette, shadow
SERVICES: Behaviour Consults, Training, Complex Skills Coaching Walking Coaching, Diet & Nutrition, Environmental Enrichment, Lifestyle and Lifestage Adaptations, Massage, Natural Health Options
BY LINE: Happy Dogs, Happy Owners
VALUES: Promoting communication and connection between dogs and their owners.
FOCUS: Nutritional guidance and environmental adaptation are often needed to complete the package and increase the success rate of training and behaviour modification.

Target Market(s)

Everyone who has a dog who they wish to improve their relationship with

Industry/Entity Type

Communication

Contact Information for Business Card

Tidal Hounds, Rosalind Vukovic, 0417 286350, tidalhounds7@quellmail.net, www.tidalhounds7.net, Qualified Dog Behavioural Trainer and Natural Animal Healthcare Consultant

Font styles to use
Sans Serif
Script

Colors
85cae6
ec2027

Requirements
Must have
• A clear indication that it is a dog services business. A raised feature
Should not have
• Pawprints, cartoons

Files

```html
<!DOCTYPE html>
<html lang="en">
<head>
<meta charset="utf-8">
<title>Tidal Hounds – Business Card Options</title>
<link rel="stylesheet" href="https://fonts.googleapis.com/css2?family=Cinzel:wght@400;700&family=Tinos&display=swap">
<style>
  :root{
    --page:#ffffff;
    --sky-top:#8fd0ec;
    --sky-mid:#4fa9d8;
    --band-light:#f4f8fb;
    --band-blue:#a9c9e6;
    --deep-top:#4b7fcf;
    --deep-bottom:#2c5cb2;
    --wave:#6fd0e6;
    --wave-soft:#9fe3f0;
    --title:#ec4a24;
    --name:#e9eef5;
    --ink:#0b1a33;
    --service:#12243f;
    --contact:#ffffff;
    --tagline:#f7a51f;
    --dog-warm:#f25c1f;
    --dog-light:#f4f6fa;
    --shadow:rgba(0,0,0,.45);
  }
  *{margin:0;padding:0;box-sizing:border-box}
  html,body{width:1200px;height:785px;overflow:hidden;background:var(--page)}
  .sheet{position:relative;width:1200px;height:785px}
  .card{
    position:absolute;width:520px;height:314px;overflow:hidden;
    background:linear-gradient(180deg,var(--sky-top) 0%,var(--sky-mid) 100%);
    box-shadow:4px 5px 7px var(--shadow);
    font-family:"Cinzel",serif;
  }
  .card--a{left:32px;top:58px}
  .card--b{left:611px;top:58px}
  .card--c{left:32px;top:416px}
  .card--d{left:611px;top:416px}
  .card__band{
    position:absolute;left:0;top:141px;width:100%;height:55px;
    background:linear-gradient(180deg,var(--band-light) 0%,#ffffff 35%,var(--band-blue) 100%);
  }
  .card__deep{
    position:absolute;left:0;top:196px;width:100%;height:118px;
    background:linear-gradient(180deg,var(--deep-top) 0%,var(--deep-bottom) 100%);
  }
  .card__waves{position:absolute;left:0;top:196px;width:520px;height:118px}
  .card__title{
    position:absolute;left:0;top:18px;width:100%;text-align:center;
    font-size:34px;font-weight:700;color:var(--title);letter-spacing:1px;line-height:1;
  }
  .card--b .card__title,.card--d .card__title{font-weight:400}
  .card__name{
    position:absolute;left:0;top:64px;width:100%;text-align:center;
    font-size:17px;color:var(--name);letter-spacing:1.5px;
    -webkit-text-stroke:.5px #2a4a73;
  }
  .card__role{
    position:absolute;left:20px;top:92px;width:480px;text-align:center;
    font-family:"Tinos",serif;font-weight:700;font-size:13px;line-height:17px;
    color:var(--ink);text-transform:uppercase;
  }
  .card__services{
    position:absolute;left:40px;top:148px;width:330px;
    font-size:12.5px;line-height:18px;color:var(--service);
  }
  .card__contact{
    position:absolute;left:33px;top:214px;
    font-family:"Tinos",serif;font-size:15px;color:var(--contact);line-height:26px;
  }
  .card__contact .label{display:inline-block;width:52px;font-size:14px}
  .card__contact .phone{font-size:17px;letter-spacing:.5px}
  .card__tagline{
    position:absolute;left:254px;top:224px;
    font-family:"Tinos",serif;font-weight:700;font-size:14px;line-height:18px;
    color:var(--tagline);text-transform:uppercase;
  }
  .card__dogs{
    position:absolute;left:383px;top:155px;width:107px;height:140px;
    background:linear-gradient(90deg,var(--dog-light) 0%,var(--dog-light) 45%,var(--dog-warm) 60%,#f69a2a 100%);
    border-radius:40px 40px 8px 8px;opacity:.92;
  }
</style>
</head>
<body>
<main class="sheet">

  <section class="card card--a">
    <div class="card__band"></div>
    <div class="card__deep"></div>
    <svg class="card__waves" viewBox="0 0 520 118" aria-hidden="true">
      <path d="M0 70 C120 30 260 40 380 70 S520 90 520 60 V118 H0Z" fill="var(--wave)" opacity=".55"/>
      <path d="M0 92 C140 60 280 70 400 95 S500 100 520 86 V118 H0Z" fill="var(--wave-soft)" opacity=".55"/>
    </svg>
    <h1 class="card__title">Tidal Hounds</h1>
    <p class="card__name">Rosalind Vukovic</p>
    <p class="card__role">Qualified Dog Behavioural Trainer and Natural Animal<br>Healthcare Consultant</p>
    <p class="card__services">Behaviour Consults, Training, Complex Skills,<br>Walking Coaching, Diet &amp; Nutrition,<br>Massage, Natural Health Options</p>
    <p class="card__contact"><span class="label">Phone</span><span class="phone">0417 286350</span><br>www.tidalhounds7.net<br>tidalhounds7@quellmail.net</p>
    <p class="card__tagline">Happy Dogs,<br>Happy Owners</p>
    <div class="card__dogs" role="img" aria-label="Two sitting dog silhouettes, one white and one red-orange"></div>
  </section>

  <section class="card card--b">
    <div class="card__band"></div>
    <div class="card__deep"></div>
    <svg class="card__waves" viewBox="0 0 520 118" aria-hidden="true">
      <path d="M0 70 C120 30 260 40 380 70 S520 90 520 60 V118 H0Z" fill="var(--wave)" opacity=".55"/>
      <path d="M0 92 C140 60 280 70 400 95 S500 100 520 86 V118 H0Z" fill="var(--wave-soft)" opacity=".55"/>
    </svg>
    <h1 class="card__title">Tidal Hounds</h1>
    <p class="card__name">Rosalind Vukovic</p>
    <p class="card__role">Qualified Dog Behavioural Trainer and Natural Animal<br>Healthcare Consultant</p>
    <p class="card__services">Behaviour Consults, Training, Complex Skills,<br>Walking Coaching, Diet &amp; Nutrition,<br>Massage, Natural Health Options</p>
    <p class="card__contact"><span class="label">Phone</span><span class="phone">0417 286350</span><br>www.tidalhounds7.net<br>tidalhounds7@quellmail.net</p>
    <p class="card__tagline">Happy Dogs,<br>Happy Owners</p>
    <div class="card__dogs" role="img" aria-label="Two sitting dog silhouettes, one white and one red-orange"></div>
  </section>

  <section class="card card--c">
    <div class="card__band"></div>
    <div class="card__deep"></div>
    <svg class="card__waves" viewBox="0 0 520 118" aria-hidden="true">
      <path d="M0 70 C120 30 260 40 380 70 S520 90 520 60 V118 H0Z" fill="var(--wave)" opacity=".55"/>
      <path d="M0 92 C140 60 280 70 400 95 S500 100 520 86 V118 H0Z" fill="var(--wave-soft)" opacity=".55"/>
    </svg>
    <h1 class="card__title">Tidal Hounds</h1>
    <p class="card__name">Rosalind Vukovic</p>
    <p class="card__role">Qualified Dog Behavioural Trainer and Natural Animal<br>Healthcare Consultant</p>
    <p class="card__services">Behaviour Consults, Training, Complex Skills,<br>Walking Coaching, Diet &amp; Nutrition,<br>Massage, Natural Health Options</p>
    <p class="card__contact"><span class="label">Phone</span><span class="phone">0417 286350</span><br>www.tidalhounds7.net<br>tidalhounds7@quellmail.net</p>
    <p class="card__tagline">Happy Dogs,<br>Happy Owners</p>
    <div class="card__dogs" role="img" aria-label="Two sitting dog silhouettes, one white and one red-orange"></div>
  </section>

  <section class="card card--d">
    <div class="card__band"></div>
    <div class="card__deep"></div>
    <svg class="card__waves" viewBox="0 0 520 118" aria-hidden="true">
      <path d="M0 70 C120 30 260 40 380 70 S520 90 520 60 V118 H0Z" fill="var(--wave)" opacity=".55"/>
      <path d="M0 92 C140 60 280 70 400 95 S500 100 520 86 V118 H0Z" fill="var(--wave-soft)" opacity=".55"/>
    </svg>
    <h1 class="card__title">Tidal Hounds</h1>
    <p class="card__name">Rosalind Vukovic</p>
    <p class="card__role">Qualified Dog Behavioural Trainer and Natural Animal<br>Healthcare Consultant</p>
    <p class="card__services">Behaviour Consults, Training, Complex Skills,<br>Walking Coaching, Diet &amp; Nutrition,<br>Massage, Natural Health Options</p>
    <p class="card__contact"><span class="label">Phone</span><span class="phone">0417 286350</span><br>www.tidalhounds7.net<br>tidalhounds7@quellmail.net</p>
    <p class="card__tagline">Happy Dogs,<br>Happy Owners</p>
    <div class="card__dogs" role="img" aria-label="Two sitting dog silhouettes, one white and one red-orange"></div>
  </section>

</main>
</body>
</html>
```